Clean and Polished Store Design

Please design a website similar to this one: http://velmarixa.com/
We require two pages:
* the home page: http://velmarixa.com/
* the product page: http://velmarixa.com/products/our-printer
Notice that there are few words and more pictures. It's clean and professional. Although I think their product page is difficult to read because it is too spread out.
Please help us generate excitement for our product via a polished and high-end looking web design. Please keep it VERY SIMPLE.
Target Market(s)
Our target market is consumers that have never bought a 3D printer before and those to whom 3D printing is new but exciting. Our market is not very technical. They love the sleek look of the printer and its ease of use.
Industry/Entity Type
Printer
Requirements
Must have
- We require two pages:
- * the home page: http://velmarixa.com/
- * the product page: http://velmarixa.com/products/our-printer
- One of our product renderings must be displayed on both the homepage and the product page.
- Our logo must be displayed on both pages.
- The pages must have a header, a footer and content equivalent to the velmarixa website.

```html
<!DOCTYPE html>
<html lang="en">
<head>
<meta charset="utf-8">
<title>Printova 3D – High Resolution Desktop 3D Printer</title>
<link href="https://fonts.googleapis.com/css2?family=Roboto+Condensed:wght@300;400;700&family=Arimo:wght@400&display=swap" rel="stylesheet">
<style>
  :root {
    --ink: #000;
    --text: #555;
    --muted: #666;
    --accent: #f07800;
    --blue: #1a8cff;
    --blue-glow: #10b4ff;
    --footer: #161616;
    --white: #fff;
    --line: #ddd;
    --social: #5a5a5a;
  }
  * { box-sizing: border-box; margin: 0; padding: 0; }
  html, body { width: 1200px; height: 1063px; overflow: hidden; background: var(--white); }
  body { position: relative; font-family: "Roboto Condensed", sans-serif; color: var(--text); }

  .top-rule { position: absolute; top: 0; left: 0; width: 1200px; height: 5px; background: var(--ink); }

  .site-header { position: absolute; top: 5px; left: 0; width: 1200px; height: 122px; }
  .brand { position: absolute; left: 129px; top: 30px; display: flex; align-items: center; gap: 12px; text-decoration: none; }
  .brand-name { font-weight: 700; font-size: 60px; line-height: 1; color: var(--ink); letter-spacing: -0.5px; }
  .brand-mark { width: 36px; height: 36px; background: var(--ink); }
  .main-nav { position: absolute; right: 110px; top: 48px; display: flex; align-items: center; }
  .main-nav a { font-size: 16px; color: var(--ink); text-decoration: none; margin-right: 39px; }
  .main-nav a:last-of-type { margin-right: 22px; }
  .cart { width: 80px; height: 37px; border: 1px solid var(--line); display: flex; align-items: center; justify-content: center; gap: 8px; font-size: 17px; color: var(--ink); }

  .hero { position: absolute; top: 127px; left: 0; width: 1200px; height: 470px;
    background: radial-gradient(ellipse 520px 330px at 330px 210px, var(--blue-glow), var(--blue)); }
  .hero-title { position: absolute; left: 140px; top: 118px; font-weight: 400; font-size: 58px; color: var(--white); line-height: 1; }
  .hero-sub { position: absolute; left: 140px; top: 182px; font-weight: 400; font-size: 35px; color: var(--white); line-height: 43px; }
  .order-btn { position: absolute; left: 140px; top: 293px; width: 140px; height: 45px; border-radius: 23px;
    background: linear-gradient(#fff, #dcdcdc); border: 1px solid #c8c8c8; font-size: 20px; color: #888;
    display: flex; align-items: center; justify-content: center; text-decoration: none; }
  .slider-dots { position: absolute; left: 140px; top: 417px; display: flex; gap: 9px; }
  .slider-dots span { width: 12px; height: 12px; border-radius: 50%; background: #1466c0; }
  .slider-dots span.active { background: var(--ink); }
  .product-render { position: absolute; left: 724px; top: 60px; width: 356px; height: 345px; border-radius: 30px;
    background: radial-gradient(circle at 40% 35%, #ffa640, #f07a00 70%, #d35f00); }

  .welcome { position: absolute; top: 620px; left: 129px; width: 460px; }
  .welcome h1 { font-weight: 400; font-size: 22px; color: var(--muted); margin-bottom: 15px; }
  .welcome .lead { font-family: "Arimo", sans-serif; font-size: 14.5px; line-height: 18px; color: var(--accent); margin-bottom: 18px; text-align: justify; }
  .welcome p { font-family: "Arimo", sans-serif; font-size: 11.5px; line-height: 18px; color: var(--text); text-align: justify; margin-bottom: 18px; }
  .video { position: absolute; left: 630px; top: 624px; width: 460px; height: 254px; background: var(--ink); }
  .video svg { position: absolute; left: 205px; top: 102px; }

  .site-footer { position: absolute; top: 940px; left: 0; width: 1200px; height: 123px; background: var(--footer); }
  .updates { position: absolute; top: 908px; left: 271px; width: 680px; height: 72px; background: var(--blue); z-index: 2; }
  .updates label { position: absolute; left: 22px; top: 19px; font-size: 30px; color: var(--white); }
  .updates input { position: absolute; left: 202px; top: 15px; width: 351px; height: 42px; border: 0; background: var(--white); }
  .updates button { position: absolute; left: 561px; top: 15px; width: 91px; height: 42px; border: 1px solid #bbb;
    background: linear-gradient(#fff, #dcdcdc); font-family: "Roboto Condensed", sans-serif; font-size: 17px; color: #888; }
  .legal { position: absolute; left: 129px; top: 79px; font-size: 11px; color: #ccc; }
  .legal a { color: #ccc; text-decoration: none; }
  .social { position: absolute; left: 1000px; top: 75px; display: flex; gap: 3px; }
  .social a { width: 20px; height: 20px; border-radius: 50%; background: var(--social); }
</style>
</head>
<body>
  <div class="top-rule"></div>

  <header class="site-header">
    <a class="brand" href="#"><span class="brand-name">Printova 3D</span><span class="brand-mark"></span></a>
    <nav class="main-nav">
      <a href="#">ABOUT</a>
      <a href="#">SUPPORT</a>
      <a href="#">STORE</a>
      <a href="#">LOGIN</a>
      <div class="cart">
        <svg width="26" height="20" viewBox="0 0 26 20" fill="none" stroke="#555" stroke-width="2">
          <path d="M1 2h4l3 12h14l2-9H7"/><circle cx="10" cy="18" r="1.5" fill="#555"/><circle cx="20" cy="18" r="1.5" fill="#555"/>
        </svg>
        <span>: 0</span>
      </div>
    </nav>
  </header>

  <section class="hero">
    <h2 class="hero-title">PRINTOVA 3D</h2>
    <p class="hero-sub">High Resolution<br>Desktop 3D Printer</p>
    <a class="order-btn" href="#">ORDER NOW!</a>
    <div class="slider-dots"><span class="active"></span><span></span><span></span></div>
    <div class="product-render" role="img" aria-label="Rendering of the orange desktop 3D printer"></div>
  </section>

  <section class="welcome">
    <h1>WELCOME!</h1>
    <p class="lead">Sed ut perspiciatis unde omnis iste natus error sit voluptatem accusantium doloremque laudantium, totam rem aperiam,</p>
    <p>Nemo enim ipsam voluptatem quia voluptas sit aspernatur aut odit aut fugit, sed quia consequuntur magni dolores eos qui ratione voluptatem sequi nesciunt. Neque porro quisquam est, qui dolorem ipsum quia dolor sit amet, consectetur, adipisci velit, sed quia non numquam eius modi tempora incidunt ut labore et dolore magnam aliquam quaerat voluptatem.</p>
    <p>Ut enim ad minima veniam, quis nostrum exercitationem ullam corporis suscipit laboriosam, nisi ut aliquid ex ea commodi consequatur? Quis autem vel eum iure reprehenderit qui in ea voluptate velit esse quam nihil molestiae consequatur</p>
  </section>

  <div class="video" role="img" aria-label="Product introduction video">
    <svg width="50" height="50" viewBox="0 0 50 50"><rect x="1" y="4" width="48" height="42" rx="10" fill="#333" stroke="#777"/><path d="M19 15l16 10-16 10z" fill="#ccc"/></svg>
  </div>

  <form class="updates">
    <label for="email">GET UPDATES</label>
    <input id="email" type="email">
    <button type="button">SUBMIT!</button>
  </form>

  <footer class="site-footer">
    <p class="legal">© PRINTOVA 2012 - <a href="#">PRIVACY POLICY</a> - <a href="#">TERMS OF SERVICE</a></p>
    <div class="social"><a href="#" aria-label="Social 1"></a><a href="#" aria-label="Social 2"></a><a href="#" aria-label="Social 3"></a><a href="#" aria-label="Social 4"></a></div>
  </footer>
</body>
</html>
```